Infographic representing workforce

Hello - I would like an infographic created to insert into a document to represent the composition of our workforce.
I've attached one very casual idea below but do NOT like the pink! Would prefer something a little more professional / modern.
Here is the information:
TOTAL EMPLOYEES
25
DIVERSITY
White: 60%
Asian: 24%
Hispanic: 8%
Middle-Eastern: 8%
AGE
25 - 44: 32%
45 - 64: 56%
65+: 12%
GENDER
Female: 60%
Male: 40%
EXECUTIVE OFFICERS
2of 3 are women
BOARD COMPOSITION
50% women (3 directors)
One woman from an unrepresented community

```html
<!DOCTYPE html>
<html lang="en">
<head>
<meta charset="utf-8">
<title>Workforce Composition Infographic</title>
<link rel="stylesheet" href="https://fonts.googleapis.com/css2?family=Bebas+Neue&family=Oswald:wght@300&display=swap">
<style>
  :root {
    --navy: #0054a6;
    --mid-blue: #0a78bb;
    --ring-blue: #0a73b8;
    --soft-blue: #7daed8;
    --pale-blue: #c8dcef;
    --band-tint: #e6f0f8;
    --paper: #ffffff;
  }
  html, body {
    margin: 0;
    padding: 0;
    width: 1200px;
    height: 951px;
    overflow: hidden;
    background: var(--paper);
  }
  .infographic { display: block; width: 1200px; height: 951px; }
  .title { font-family: "Bebas Neue", sans-serif; fill: var(--paper); font-size: 128px; }
  .headcount { font-family: "Bebas Neue", sans-serif; fill: var(--navy); font-size: 126px; }
  .pill-outer { fill: var(--ring-blue); }
  .pill-gap { fill: var(--paper); }
  .pill-core { fill: var(--navy); }
  .pill-label { font-family: "Bebas Neue", sans-serif; fill: var(--paper); text-anchor: middle; }
  .pill-label--section { font-size: 42px; }
  .pill-label--lower { font-size: 44px; }
  .divider { stroke: var(--soft-blue); stroke-width: 3; }
  .leader { stroke: var(--navy); stroke-width: 1; fill: none; }
  .leader-dot { fill: var(--navy); }
  .label { font-family: "Bebas Neue", sans-serif; fill: var(--navy); font-size: 27px; }
  .value { font-family: "Oswald", sans-serif; font-weight: 300; fill: var(--soft-blue); font-size: 24px; }
  .value--large { font-size: 30px; }
  .caption { font-family: "Bebas Neue", sans-serif; fill: var(--navy); font-size: 40px; }
  .footnote { font-family: "Oswald", sans-serif; font-weight: 300; fill: var(--soft-blue); font-size: 17px; }
  .slice { stroke: var(--paper); stroke-width: 3; stroke-linejoin: round; }
  .slice--navy { fill: var(--navy); }
  .slice--mid { fill: var(--mid-blue); }
  .slice--soft { fill: var(--soft-blue); }
  .slice--pale { fill: var(--pale-blue); }
  .figure--male { fill: var(--navy); }
  .figure--female { fill: var(--soft-blue); }
  .figure--mid { fill: var(--mid-blue); }
  .figure--white { fill: var(--paper); }
</style>
</head>
<body>
<svg class="infographic" viewBox="0 0 1200 951" xmlns="http://www.w3.org/2000/svg">

  <!-- Header -->
  <g class="header">
    <rect x="0" y="0" width="1200" height="121" fill="var(--navy)"/>
    <text class="title" x="253" y="111" textLength="688" lengthAdjust="spacingAndGlyphs">TOTAL EMPLOYEES</text>
  </g>

  <!-- Headcount band -->
  <g class="headcount-band">
    <rect x="0" y="121" width="1200" height="119" fill="var(--band-tint)"/>
    <text class="headcount" x="76" y="223" textLength="78" lengthAdjust="spacingAndGlyphs">25</text>
    <g class="headcount-row" role="img" aria-label="Row of 25 employee figures: 15 men and 10 women">
      <rect class="figure--male" x="170" y="139" width="30" height="84" rx="8"/>
      <rect class="figure--male" x="207" y="139" width="30" height="84" rx="8"/>
      <rect class="figure--female" x="245" y="139" width="30" height="84" rx="8"/>
      <rect class="figure--male" x="283" y="139" width="30" height="84" rx="8"/>
      <rect class="figure--male" x="320" y="139" width="30" height="84" rx="8"/>
      <rect class="figure--male" x="356" y="139" width="30" height="84" rx="8"/>
      <rect class="figure--female" x="394" y="139" width="30" height="84" rx="8"/>
      <rect class="figure--male" x="434" y="139" width="30" height="84" rx="8"/>
      <rect class="figure--male" x="471" y="139" width="30" height="84" rx="8"/>
      <rect class="figure--male" x="508" y="139" width="30" height="84" rx="8"/>
      <rect class="figure--male" x="544" y="139" width="30" height="84" rx="8"/>
      <rect class="figure--female" x="584" y="139" width="30" height="84" rx="8"/>
      <rect class="figure--male" x="623" y="139" width="30" height="84" rx="8"/>
      <rect class="figure--male" x="662" y="139" width="30" height="84" rx="8"/>
      <rect class="figure--male" x="699" y="139" width="30" height="84" rx="8"/>
      <rect class="figure--female" x="737" y="139" width="30" height="84" rx="8"/>
      <rect class="figure--female" x="777" y="139" width="30" height="84" rx="8"/>
      <rect class="figure--female" x="818" y="139" width="30" height="84" rx="8"/>
      <rect class="figure--female" x="858" y="139" width="30" height="84" rx="8"/>
      <rect class="figure--male" x="897" y="139" width="30" height="84" rx="8"/>
      <rect class="figure--female" x="936" y="139" width="30" height="84" rx="8"/>
      <rect class="figure--female" x="977" y="139" width="30" height="84" rx="8"/>
      <rect class="figure--female" x="1017" y="139" width="30" height="84" rx="8"/>
      <rect class="figure--male" x="1056" y="139" width="30" height="84" rx="8"/>
      <rect class="figure--male" x="1093" y="139" width="30" height="84" rx="8"/>
    </g>
  </g>

  <!-- Section dividers -->
  <line class="divider" x1="405" y1="271" x2="405" y2="605"/>
  <line class="divider" x1="774" y1="271" x2="774" y2="605"/>
  <line class="divider" x1="578" y1="651" x2="578" y2="924"/>

  <!-- Diversity -->
  <g class="section section--diversity">
    <g class="pill">
      <rect class="pill-outer" x="110" y="272" width="202" height="66" rx="33"/>
      <rect class="pill-gap" x="115" y="277" width="192" height="56" rx="28"/>
      <rect class="pill-core" x="119" y="281" width="184" height="48" rx="24"/>
      <text class="pill-label pill-label--section" x="211" y="321">DIVERSITY</text>
    </g>
    <g class="pie">
      <path class="slice slice--navy" d="M207 447 L124.5 467.6 A85 85 0 1 1 285.8 478.9 Z"/>
      <path class="slice slice--mid" d="M207 447 L285.8 478.9 A85 85 0 0 1 180.7 527.8 Z"/>
      <path class="slice slice--soft" d="M207 447 L180.7 527.8 A85 85 0 0 1 144.8 505 Z"/>
      <path class="slice slice--pale" d="M207 447 L144.8 505 A85 85 0 0 1 124.5 467.6 Z"/>
    </g>
    <g class="callout">
      <line class="leader" x1="210" y1="412" x2="365" y2="412"/>
      <circle class="leader-dot" cx="210" cy="412" r="3.5"/>
      <text class="label" x="302" y="410" textLength="44" lengthAdjust="spacingAndGlyphs">WHITE</text>
      <text class="value" x="302" y="437" textLength="31" lengthAdjust="spacingAndGlyphs">60%</text>
    </g>
    <g class="callout">
      <line class="leader" x1="242" y1="503" x2="365" y2="503"/>
      <circle class="leader-dot" cx="242" cy="503" r="3.5"/>
      <text class="label" x="306" y="499" textLength="40" lengthAdjust="spacingAndGlyphs">ASIAN</text>
      <text class="value" x="306" y="526" textLength="30" lengthAdjust="spacingAndGlyphs">24%</text>
    </g>
    <g class="callout">
      <line class="leader" x1="47" y1="483" x2="142" y2="483"/>
      <circle class="leader-dot" cx="142" cy="483" r="3.5"/>
      <text class="label" x="47" y="480" textLength="64" lengthAdjust="spacingAndGlyphs">HISPANIC</text>
      <text class="value" x="47" y="505" textLength="21" lengthAdjust="spacingAndGlyphs">8%</text>
    </g>
    <g class="callout">
      <polyline class="leader" points="169,506 169,581 295,581"/>
      <circle class="leader-dot" cx="169" cy="506" r="3.5"/>
      <text class="label" x="174" y="577" textLength="119" lengthAdjust="spacingAndGlyphs">MIDDLE EASTERN</text>
      <text class="value" x="174" y="606" textLength="21" lengthAdjust="spacingAndGlyphs">8%</text>
    </g>
  </g>

  <!-- Gender -->
  <g class="section section--gender">
    <g class="pill">
      <rect class="pill-outer" x="508" y="272" width="167" height="66" rx="33"/>
      <rect class="pill-gap" x="513" y="277" width="157" height="56" rx="28"/>
      <rect class="pill-core" x="517" y="281" width="149" height="48" rx="24"/>
      <text class="pill-label pill-label--section" x="591" y="321">GENDER</text>
    </g>
    <g class="pie">
      <path class="slice slice--navy" d="M589 447 L589 362 A85 85 0 0 1 639 515.8 Z"/>
      <path class="slice slice--mid" d="M589 447 L639 515.8 A85 85 0 1 1 589 362 Z"/>
      <rect class="figure--white" x="538" y="398" width="28" height="64" rx="8" role="img" aria-label="Female figure icon"/>
      <rect class="figure--white" x="613" y="420" width="26" height="65" rx="8" role="img" aria-label="Male figure icon"/>
    </g>
    <g class="callout">
      <line class="leader" x1="444" y1="446" x2="521" y2="446"/>
      <circle class="leader-dot" cx="521" cy="446" r="3.5"/>
      <text class="label" x="444" y="441" textLength="54" lengthAdjust="spacingAndGlyphs">FEMALE</text>
      <text class="value" x="444" y="468" textLength="31" lengthAdjust="spacingAndGlyphs">60%</text>
    </g>
    <g class="callout">
      <line class="leader" x1="653" y1="449" x2="733" y2="449"/>
      <circle class="leader-dot" cx="653" cy="449" r="3.5"/>
      <text class="label" x="686" y="445" textLength="38" lengthAdjust="spacingAndGlyphs">MALE</text>
      <text class="value" x="686" y="472" textLength="31" lengthAdjust="spacingAndGlyphs">40%</text>
    </g>
  </g>

  <!-- Age -->
  <g class="section section--age">
    <g class="pill">
      <rect class="pill-outer" x="903" y="272" width="110" height="66" rx="33"/>
      <rect class="pill-gap" x="908" y="277" width="100" height="56" rx="28"/>
      <rect class="pill-core" x="912" y="281" width="92" height="48" rx="24"/>
      <text class="pill-label pill-label--section" x="958" y="321">AGE</text>
    </g>
    <g class="pie">
      <path class="slice slice--navy" d="M962 447 L911.6 515.4 A85 85 0 1 1 1034.1 402 Z"/>
      <path class="slice slice--soft" d="M962 447 L1034.1 402 A85 85 0 0 1 1045.4 463.5 Z"/>
      <path class="slice slice--mid" d="M962 447 L1045.4 463.5 A85 85 0 0 1 911.6 515.4 Z"/>
    </g>
    <g class="figure-pair" role="img" aria-label="Man and woman figures, age 45 to 64">
      <rect class="figure--male" x="815" y="369" width="26" height="65" rx="7"/>
      <rect class="figure--mid" x="845" y="369" width="28" height="65" rx="7"/>
    </g>
    <g class="figure-pair" role="img" aria-label="Older man and woman figures with canes, age 65 and over">
      <rect class="figure--male" x="1110" y="393" width="27" height="66" rx="7"/>
      <rect class="figure--mid" x="1142" y="393" width="32" height="66" rx="7"/>
    </g>
    <g class="figure-pair" role="img" aria-label="Man and woman figures, age 25 to 44">
      <rect class="figure--male" x="1069" y="526" width="26" height="65" rx="7"/>
      <rect class="figure--mid" x="1099" y="526" width="28" height="65" rx="7"/>
    </g>
    <g class="callout">
      <line class="leader" x1="820" y1="461" x2="923" y2="461"/>
      <circle class="leader-dot" cx="923" cy="461" r="3.5"/>
      <text class="label" x="820" y="458" textLength="45" lengthAdjust="spacingAndGlyphs">45-64</text>
      <text class="value" x="820" y="483" textLength="31" lengthAdjust="spacingAndGlyphs">56%</text>
    </g>
    <g class="callout">
      <line class="leader" x1="1028" y1="431" x2="1103" y2="431"/>
      <circle class="leader-dot" cx="1028" cy="431" r="3.5"/>
      <text class="label" x="1061" y="429" textLength="28" lengthAdjust="spacingAndGlyphs">65+</text>
      <text class="value" x="1061" y="455" textLength="31" lengthAdjust="spacingAndGlyphs">12%</text>
    </g>
    <g class="callout">
      <polyline class="leader" points="991,498 991,554 1064,554"/>
      <circle class="leader-dot" cx="991" cy="498" r="3.5"/>
      <text class="label" x="1002" y="551" textLength="45" lengthAdjust="spacingAndGlyphs">25-44</text>
      <text class="value" x="1002" y="577" textLength="31" lengthAdjust="spacingAndGlyphs">32%</text>
    </g>
  </g>

  <!-- Executive officers -->
  <g class="section section--executives">
    <g class="pill">
      <rect class="pill-outer" x="225" y="654" width="308" height="68" rx="34"/>
      <rect class="pill-gap" x="230" y="659" width="298" height="58" rx="29"/>
      <rect class="pill-core" x="234" y="663" width="290" height="50" rx="25"/>
      <text class="pill-label pill-label--lower" x="379" y="705" textLength="250" lengthAdjust="spacingAndGlyphs">EXECUTIVE OFFICERS</text>
    </g>
    <g class="officer-figures" role="img" aria-label="Three executive figures: one man in a suit and two women">
      <rect class="figure--male" x="265" y="732" width="69" height="142" rx="14"/>
      <rect class="figure--mid" x="341" y="734" width="63" height="140" rx="14"/>
      <rect class="figure--mid" x="408" y="734" width="64" height="140" rx="14"/>
    </g>
    <text class="caption" x="274" y="910" textLength="187" lengthAdjust="spacingAndGlyphs">2 OF 3 ARE WOMEN</text>
  </g>

  <!-- Board composition -->
  <g class="section section--board">
    <g class="pill">
      <rect class="pill-outer" x="629" y="654" width="311" height="68" rx="34"/>
      <rect class="pill-gap" x="634" y="659" width="301" height="58" rx="29"/>
      <rect class="pill-core" x="638" y="663" width="293" height="50" rx="25"/>
      <text class="pill-label pill-label--lower" x="785" y="705" textLength="253" lengthAdjust="spacingAndGlyphs">BOARD COMPOSITION</text>
    </g>
    <g class="pie">
      <path class="slice slice--navy" d="M711.5 733 A84 84 0 0 0 711.5 901 Z" stroke-width="0"/>
      <path class="slice slice--mid" d="M714.5 733 A84 84 0 0 1 714.5 901 Z" stroke-width="0"/>
      <rect class="figure--white" x="654" y="767" width="46" height="96" rx="10" role="img" aria-label="Male director figure icon"/>
      <rect class="figure--white" x="725" y="767" width="43" height="96" rx="10" role="img" aria-label="Female director figure icon"/>
    </g>
    <g class="callout">
      <line class="leader" x1="781" y1="792" x2="893" y2="792"/>
      <circle class="leader-dot" cx="781" cy="792" r="3.5"/>
      <text class="label" x="808" y="788" textLength="62" lengthAdjust="spacingAndGlyphs">WOMEN</text>
      <text class="value value--large" x="808" y="818" textLength="35" lengthAdjust="spacingAndGlyphs">50%</text>
    </g>
    <g class="callout">
      <line class="leader" x1="755" y1="876" x2="901" y2="876"/>
      <circle class="leader-dot" cx="755" cy="876" r="3.5"/>
      <text class="label" x="800" y="872" textLength="99" lengthAdjust="spacingAndGlyphs">3 DIRECTORS</text>
      <text class="footnote" x="785" y="896" textLength="288" lengthAdjust="spacingAndGlyphs">ONE WOMAN FROM AN UNREPRESENTED COMMUNITY</text>
    </g>
  </g>
</svg>
</body>
</html>
```